Uprising SaaS company needs an attractive business card design

We're an uprising SaaS company who's attempting to attack the rigid car (insurance) claims management market in Europe.
We want to our mighty base order management system, listen to our clients to connect the smart ideas to build something even mightier.
We primarily focus on helping our customers manage their customers' claims/orders and get them resolved as smoothly as possible.
We'd like the business card design to express technical innovation and the fact that we connect smart ideas, as our company slogan indicates.
Contact Information for Business Card
Name, position, website, email, mobile, business address
Font styles to use
Colors
Designer to choose colors to be used in the design.
Look and feel
Each slider illustrates characteristics of the customer's brand and the style your logo design should communicate.

```html
<!DOCTYPE html>
<html lang="en">
<head>
<meta charset="utf-8">
<title>claimora business card</title>
<link rel="stylesheet" href="https://fonts.googleapis.com/css2?family=Questrial&display=swap">
<style>
  :root {
    --backdrop: #4a4a4a;
    --card: #1e1e1e;
    --accent: #6ccbe6;
    --accent-deep: #1478b8;
    --text-grey: #8c8c8c;
    --rule-grey: #7a7a7a;
  }
  * { margin: 0; padding: 0; box-sizing: border-box; }
  html, body {
    width: 1200px;
    height: 900px;
    overflow: hidden;
    background: var(--backdrop);
    font-family: "Questrial", "Century Gothic", sans-serif;
  }
  .canvas {
    position: relative;
    width: 1200px;
    height: 900px;
  }
  .card {
    position: absolute;
    left: 250px;
    width: 700px;
    height: 388px;
    background: var(--card);
    box-shadow: 0 10px 24px rgba(0,0,0,0.35);
  }
  .card--front { top: 42px; }
  .card--back { top: 470px; }

  .brand-name {
    color: var(--accent);
    font-weight: 400;
    letter-spacing: 1px;
    line-height: 1;
    white-space: nowrap;
  }
  .card--front .brand-name {
    position: absolute;
    left: 0;
    right: 0;
    top: 50%;
    transform: translateY(-50%);
    text-align: center;
    font-size: 104px;
  }
  .card--back .brand-name {
    position: absolute;
    right: 29px;
    top: 58px;
    font-size: 54px;
  }

  .holder {
    position: absolute;
    left: 26px;
    top: 212px;
  }
  .holder__name {
    color: var(--accent);
    font-size: 28px;
    line-height: 1;
    letter-spacing: 0.3px;
  }
  .holder__role {
    color: var(--accent);
    font-size: 19px;
    line-height: 1;
    margin-top: 4px;
  }
  .holder__rule {
    position: absolute;
    left: 26px;
    top: 266px;
    width: 302px;
    height: 2px;
    background: linear-gradient(to right, var(--rule-grey), var(--accent-deep));
  }

  .contact-list {
    position: absolute;
    left: 26px;
    top: 292px;
    list-style: none;
  }
  .contact-list__item {
    display: flex;
    align-items: center;
    gap: 8px;
    color: var(--text-grey);
    font-size: 19px;
    line-height: 1;
    height: 25px;
  }
  .contact-list__item + .contact-list__item { margin-top: 5px; }
  .contact-list__item:first-child { margin-bottom: 6px; }
  .contact-icon {
    width: 22px;
    height: 20px;
    flex: none;
  }

  .address {
    position: absolute;
    right: 29px;
    top: 322px;
    color: var(--text-grey);
    font-size: 19px;
    line-height: 25px;
    font-style: normal;
    letter-spacing: 0.4px;
  }
</style>
</head>
<body>
<main class="canvas">
  <section class="card card--front" aria-label="Card front">
    <div class="brand-name">claimora</div>
  </section>

  <section class="card card--back" aria-label="Card back">
    <div class="brand-name">claimora</div>

    <div class="holder">
      <p class="holder__name">JONAS KELLER</p>
      <p class="holder__role">Managing Director</p>
    </div>
    <div class="holder__rule"></div>

    <ul class="contact-list">
      <li class="contact-list__item">
        <svg class="contact-icon" viewBox="0 0 22 20" aria-hidden="true">
          <rect x="6" y="1" width="10" height="18" rx="1.5" fill="none" stroke="var(--accent)" stroke-width="1.6"/>
          <rect x="8" y="3.5" width="6" height="5" fill="var(--accent)"/>
          <g fill="var(--accent)">
            <rect x="8" y="10.5" width="1.6" height="1.6"/><rect x="10.2" y="10.5" width="1.6" height="1.6"/><rect x="12.4" y="10.5" width="1.6" height="1.6"/>
            <rect x="8" y="13" width="1.6" height="1.6"/><rect x="10.2" y="13" width="1.6" height="1.6"/><rect x="12.4" y="13" width="1.6" height="1.6"/>
            <rect x="8" y="15.5" width="1.6" height="1.6"/><rect x="10.2" y="15.5" width="1.6" height="1.6"/><rect x="12.4" y="15.5" width="1.6" height="1.6"/>
          </g>
        </svg>
        <span>+49 170 5550142</span>
      </li>
      <li class="contact-list__item">
        <svg class="contact-icon" viewBox="0 0 22 20" aria-hidden="true">
          <rect x="1" y="4" width="20" height="13" fill="var(--accent)"/>
          <path d="M1 4 L11 12 L21 4 M1 17 L8 10 M21 17 L14 10" fill="none" stroke="var(--card)" stroke-width="1.3"/>
        </svg>
        <span>info@claimora.com</span>
      </li>
      <li class="contact-list__item">
        <svg class="contact-icon" viewBox="0 0 22 20" aria-hidden="true">
          <g fill="none" stroke="var(--accent)" stroke-width="1.4">
            <circle cx="11" cy="10" r="8.5"/>
            <ellipse cx="11" cy="10" rx="4" ry="8.5"/>
            <line x1="2.5" y1="10" x2="19.5" y2="10"/>
            <line x1="11" y1="1.5" x2="11" y2="18.5"/>
            <path d="M4 5.5 H18 M4 14.5 H18"/>
          </g>
        </svg>
        <span>www.claimora.com</span>
      </li>
    </ul>

    <address class="address">
      Lindenweg 14b<br>
      10115 Berlin, Germany
    </address>
  </section>
</main>
</body>
</html>
```